Carwash Signage

We own and operate a 25m tunnel car wash in the uk. We are looking to upgrade our signage to include the following:-

Wash selection Board Size-1300x1300mm
Conditions 1300x1300mm
Instructions 1300x1300mm
Banner 2600x600mm
Stamp card flyer a5 double sided - 9 squares for stamping 3rd square needs to say free air freshener 9th square needs to say free vip car wash.

I have attached some notes for the details that are required to be included.

We are looking for a modern smart look more European car wash style than American car wash style. It should be bold and clear. with yellow/orange & blue/green,grey colours

The final design must be in a industry standard printable format.

UPDATED BRIEF AS DISCUSSED: We require design for 2 x window decals, flag design and 50% off voucher. Attached are rough layout drawings of what they should look like - we expect the designs to be in keeping with the previous designs colours, etc that have been carried out. We Look forward to hearing from you.

Target Market(s)

local car owners within a 15-20 mile radius

Colors
0054AA
0677BA
7BADD7
CADEEF
E8F1F8
0094D4
00A9DD
6FCCEA
C7EBF8
E9F6FB
00AB8E
00BBA5
67D7C9
C6EFE9
E9F9F6

Requirements
Must have
• must be sharp and modern European look

```html
<!DOCTYPE html>
<html lang="en">
<head>
<meta charset="UTF-8">
<title>Attended Car Wash Banner</title>
<link rel="stylesheet" href="https://fonts.googleapis.com/css2?family=Anton&family=Bebas+Neue&display=swap">
<style>
  :root {
    --brand-blue: #0A24C2;
    --bar-grey: #414042;
    --paper: #FFFFFF;
    --soft-blue: #C7D4F8;
    --icon-grey: #3F3F42;
  }
  html, body {
    margin: 0;
    padding: 0;
    width: 1200px;
    height: 277px;
    overflow: hidden;
    background: var(--paper);
  }
  .banner {
    position: relative;
    width: 1200px;
    height: 277px;
    overflow: hidden;
    background: var(--brand-blue);
    font-family: "Bebas Neue", sans-serif;
  }
  .banner__wave {
    position: absolute;
    left: 0;
    top: 0;
    width: 1200px;
    height: 277px;
  }
  .banner__kicker {
    position: absolute;
    left: 23px;
    top: 17px;
    margin: 0;
    font-family: "Anton", sans-serif;
    font-size: 37px;
    line-height: 1;
    color: var(--paper);
    letter-spacing: 0.5px;
  }
  .banner__headline {
    position: absolute;
    left: 199px;
    top: 55px;
    margin: 0;
    font-family: "Anton", sans-serif;
    font-weight: 400;
    font-size: 166px;
    line-height: 1;
    color: var(--brand-blue);
    letter-spacing: 3px;
    white-space: nowrap;
  }
  .brand {
    position: absolute;
    right: 17px;
    top: 22px;
    display: flex;
    align-items: center;
    gap: 8px;
  }
  .brand__dot {
    width: 26px;
    height: 26px;
    border-radius: 50%;
    background: var(--paper);
  }
  .brand__name {
    font-family: "Bebas Neue", sans-serif;
    font-size: 34px;
    line-height: 1;
    color: var(--paper);
    letter-spacing: 1px;
    white-space: nowrap;
  }
  .hours-visual {
    position: absolute;
    left: 940px;
    top: 104px;
    width: 170px;
    height: 106px;
    border-radius: 53px;
    background: radial-gradient(circle at 45% 55%, var(--soft-blue) 0%, #8A97C8 55%, var(--icon-grey) 100%);
  }
  .hours-title {
    position: absolute;
    right: 17px;
    top: 190px;
    margin: 0;
    font-family: "Bebas Neue", sans-serif;
    font-size: 29px;
    line-height: 1;
    color: var(--brand-blue);
    letter-spacing: 0.5px;
  }
  .info-bar {
    position: absolute;
    left: 0;
    top: 217px;
    width: 1200px;
    height: 60px;
    background: var(--bar-grey);
  }
  .payments {
    position: absolute;
    left: 35px;
    top: 11px;
    margin: 0;
    font-size: 39px;
    line-height: 1;
    color: var(--paper);
    letter-spacing: 0.3px;
    white-space: nowrap;
  }
  .card-icon {
    position: absolute;
    left: 509px;
    top: 6px;
    width: 76px;
    height: 46px;
  }
  .hours-list {
    position: absolute;
    right: 17px;
    top: 9px;
    margin: 0;
    display: grid;
    grid-template-columns: auto 26px auto;
    row-gap: 0;
    font-size: 24px;
    line-height: 24px;
    color: var(--paper);
  }
  .hours-list dt { text-align: right; }
  .hours-list .sep { text-align: center; }
  .hours-list dd { margin: 0; text-align: right; }
</style>
</head>
<body>
  <div class="banner">
    <svg class="banner__wave" viewBox="0 0 1200 277" aria-hidden="true">
      <path d="M0 90 C 10 84, 30 82, 60 82 C 200 80, 300 50, 430 22 C 520 8, 600 14, 700 38 C 850 72, 1000 80, 1080 100 C 1140 112, 1180 130, 1200 145 L 1200 277 L 0 277 Z" fill="#FFFFFF"/>
    </svg>

    <p class="banner__kicker">ATTENDED</p>
    <h1 class="banner__headline">CAR WASH</h1>

    <div class="brand">
      <span class="brand__dot"></span>
      <span class="brand__name">BRIGHTWAY CAR WASH</span>
    </div>

    <div class="hours-visual" role="img" aria-label="Stopwatch with gears illustrating opening times"></div>
    <p class="hours-title">OPEN TIMING</p>

    <div class="info-bar">
      <p class="payments">CASH + CARD PAYMENTS ACCEPTED</p>
      <svg class="card-icon" viewBox="0 0 76 46" aria-hidden="true">
        <rect x="0" y="0" width="76" height="46" rx="3" fill="#FFFFFF"/>
        <rect x="6" y="14" width="64" height="7" fill="#0A24C2"/>
        <rect x="6" y="28" width="25" height="2.5" fill="#0A24C2"/>
        <rect x="6" y="33" width="25" height="2.5" fill="#0A24C2"/>
        <circle cx="47" cy="34" r="4" fill="#0A24C2"/>
        <circle cx="54" cy="34" r="4" fill="#0A24C2"/>
        <circle cx="61" cy="34" r="4" fill="#0A24C2"/>
      </svg>
      <dl class="hours-list">
        <dt>MON-SAT</dt><span class="sep">–</span><dd>8:00 - 18:00</dd>
        <dt>SUN</dt><span class="sep">–</span><dd>9:00 - 18:00</dd>
      </dl>
    </div>
  </div>
</body>
</html>
```